Business Stationery - Business Cards - Letterheads, Compliment Slips

We need a new set of artwork designed for our client, they are a Construction Company, that also sell Kitchens, bathrooms and appliances.
They are an up and comping company that focus on quality and bespoke build. For them it is all about the quality of what they install, build or design. They have recently been awarded sole distributorship of a German kitchen brand Annelore Kuchen.
We need to present a quick job to them and provide some proofs for their new Artwork which encompasses all the elements of the company
The company name is the Halvorn Group and we need to design a logo also.
Any Questions please let me know asap

Target Market(s)
Upmarket clients, or small Development companies.
Industry/Entity Type
Business
Look and feel

```html
<!DOCTYPE html>
<html lang="en">
<head>
<meta charset="utf-8">
<title>Halvorn Group – Stationery Set</title>
<link rel="stylesheet" href="https://fonts.googleapis.com/css2?family=Arimo:wght@400;700&family=Montserrat:wght@400;600;700&display=swap">
<style>
  :root {
    --bg: #ececec;
    --ink-black: #161616;
    --ink-deep: #0f0f0f;
    --band-grey: #6b645d;
    --paper-top: #f4ede9;
    --paper-bottom: #e9ddd6;
    --brand-green: #4fb89a;
    --text-dark: #2a2a2a;
    --text-light: #f1f1f1;
    --text-muted: #a9a9a9;
    --rule: #4a4a4a;
  }
  * { box-sizing: border-box; margin: 0; padding: 0; }
  html, body { width: 1200px; height: 900px; overflow: hidden; }
  body { background: var(--bg); font-family: "Arimo", Arial, sans-serif; position: relative; }

  .brand {
    font-family: "Montserrat", Arial, sans-serif;
    font-weight: 600;
    color: var(--brand-green);
    display: flex; align-items: center; gap: 7px;
    letter-spacing: 0.04em;
    white-space: nowrap;
  }
  .brand__dot { width: 9px; height: 9px; border-radius: 50%; background: var(--brand-green); }

  /* Letterhead */
  .letterhead {
    position: absolute; left: 60px; top: 100px; width: 440px; height: 622px;
    background: linear-gradient(160deg, var(--paper-top), var(--paper-bottom));
    box-shadow: 0 3px 10px rgba(0,0,0,0.12);
    color: var(--text-dark);
  }
  .letterhead .brand { position: absolute; left: 30px; top: 30px; font-size: 15px; }
  .letter {
    position: absolute; left: 112px; top: 92px; width: 300px;
    font-size: 10.5px; line-height: 1.85;
  }
  .letter p { margin-bottom: 10px; }
  .letter__sign { margin-top: 46px; padding-left: 70px; }
  .letterhead__address {
    position: absolute; left: 30px; bottom: 34px;
    font-size: 11px; line-height: 1.55; font-style: normal;
  }

  /* Compliment slip & envelope */
  .slip, .envelope {
    position: absolute; left: 560px; width: 580px; height: 250px;
    background: var(--ink-black); overflow: hidden;
    box-shadow: 0 3px 10px rgba(0,0,0,0.18);
  }
  .slip { top: 60px; }
  .envelope { top: 340px; }
  .slip__band, .card__band, .envelope__flap { position: absolute; inset: 0; width: 100%; height: 100%; }
  .slip .brand { position: absolute; right: 30px; top: 26px; font-size: 17px; }
  .slip__address {
    position: absolute; right: 30px; bottom: 26px;
    font-size: 10px; line-height: 1.45; text-align: right;
    color: var(--text-light); font-style: normal;
  }

  /* Business cards */
  .card {
    position: absolute; top: 630px; width: 270px; height: 170px;
    background: var(--ink-black); overflow: hidden;
    box-shadow: 0 3px 10px rgba(0,0,0,0.18);
    color: var(--text-light);
  }
  .card--front { left: 560px; }
  .card--back { left: 870px; }
  .card--front .brand { position: absolute; right: 24px; top: 72px; font-size: 16px; }

  .card__name {
    position: absolute; left: 20px; top: 24px;
    font-family: "Montserrat", Arial, sans-serif;
  }
  .card__name h2 { font-size: 15px; font-weight: 700; letter-spacing: 0.01em; }
  .card__name p { font-size: 9px; font-weight: 600; margin-top: 2px; }
  .card__contact {
    position: absolute; left: 20px; top: 80px; list-style: none;
    font-size: 7.5px; line-height: 1; color: var(--text-muted);
  }
  .card__contact li { display: flex; align-items: center; gap: 6px; margin-bottom: 6px; }
  .card__divider { position: absolute; left: 146px; top: 58px; width: 1px; height: 92px; background: var(--rule); }
  .card__address {
    position: absolute; left: 156px; top: 60px; display: flex; gap: 6px;
    font-size: 7.5px; line-height: 1.45; color: var(--text-muted); font-style: normal;
  }
  .icon { width: 8px; height: 8px; flex: none; fill: var(--text-muted); }
</style>
</head>
<body>

  <section class="letterhead" aria-label="Letterhead">
    <div class="brand"><span class="brand__dot"></span>Halvorn Group</div>
    <div class="letter">
      <p>Dear All</p>
      <p>Lorem ipsum dolor sit amet, audiam habemus democritum an vix. Te pro aliquam accommodare. Cum ut eirmod albucius, omnis tincidunt sententiae vis ea, an mel eius intellegebat. Te his fugit primis contentiones, percipit prodesset eu vim, eripuit omittam torquatos ea est. Ullum utinam in qui.</p>
      <p>Quo in mandamus iracundia efficiantur. Pro quod ridens animal ut, mel et antiopam abhorreant. Et alii ornatus vis, causae iuvaret est eu, ad primis noster tamquam has. Enim dicunt offendit per ut, sea tale sonet percipit et, sed an natum doming. At ius assum inciderint.</p>
      <p>Minimum mediocritatem ad mei. Pri accusamus democritum an. Te quo debet noster accusata, vix et agam option reprehendunt. Duis persius eam ea. In vitae facete lucilius vel.</p>
      <p>Sea ex vocent honestatis, intellegam efficiantur ex mea. Commodo dissentiunt philosophia has ad, erant dissentias ut vel. Saepe legere eam ei, justo congue vel ex, mundi percipit ei vis. Pri illud iuvaret ea, causa.</p>
      <p class="letter__sign">Tobias Renfrew</p>
    </div>
    <address class="letterhead__address">Halvorn Kitchens<br>48 Marlow Street<br>Eastbridge<br>EB4 2KL</address>
  </section>

  <section class="slip" aria-label="Compliment slip">
    <svg class="slip__band" viewBox="0 0 580 250" preserveAspectRatio="none" aria-hidden="true">
      <path d="M0 0 H250 C140 40 70 130 40 250 H0 Z" fill="var(--band-grey)"/>
      <path d="M262 0 C150 45 84 135 56 250 H40 C70 130 140 40 250 0 Z" fill="var(--ink-black)"/>
    </svg>
    <div class="brand"><span class="brand__dot"></span>Halvorn Group</div>
    <address class="slip__address">Halvorn Kitchens<br>48 Marlow Street<br>Eastbridge<br>EB4 2KL</address>
  </section>

  <section class="envelope" aria-label="Envelope back">
    <svg class="envelope__flap" viewBox="0 0 580 250" preserveAspectRatio="none" aria-hidden="true">
      <path d="M0 0 H580 V8 L330 105 Q290 120 250 105 L0 8 Z" fill="var(--ink-deep)"/>
    </svg>
  </section>

  <section class="card card--front" aria-label="Business card front">
    <svg class="card__band" viewBox="0 0 270 170" preserveAspectRatio="none" aria-hidden="true">
      <path d="M0 0 H140 C80 20 40 60 22 110 C12 80 6 40 0 20 Z" fill="var(--band-grey)"/>
    </svg>
    <div class="brand"><span class="brand__dot"></span>Halvorn Group</div>
  </section>

  <section class="card card--back" aria-label="Business card back">
    <div class="card__name">
      <h2>Tobias Renfrew</h2>
      <p>Design Consultant</p>
    </div>
    <ul class="card__contact">
      <li><svg class="icon" viewBox="0 0 10 10"><path d="M2 0.5 L3.6 2.6 L2.8 3.6 Q4 6 6.4 7.2 L7.4 6.4 L9.5 8 L8.4 9.5 Q3.5 9 0.5 1.6 Z"/></svg>020 7946 0381</li>
      <li><svg class="icon" viewBox="0 0 10 10"><rect x="2.5" y="0.5" width="5" height="3"/><rect x="0.5" y="3.8" width="9" height="4"/><rect x="2.5" y="7" width="5" height="2.5"/></svg>020 7946 0382</li>
      <li><svg class="icon" viewBox="0 0 10 10"><path d="M0.5 2 H9.5 V8.5 H0.5 Z M0.8 2.3 L5 5.6 L9.2 2.3" stroke="var(--ink-black)" stroke-width="0.8"/></svg>info@halvorn.co.uk</li>
      <li><svg class="icon" viewBox="0 0 10 10"><circle cx="5" cy="5" r="4.5"/></svg>www.halvorn.co.uk</li>
    </ul>
    <span class="card__divider"></span>
    <address class="card__address">
      <svg class="icon" viewBox="0 0 10 10"><path d="M5 0.5 A3.3 3.3 0 0 1 8.3 3.8 C8.3 6 5 9.5 5 9.5 C5 9.5 1.7 6 1.7 3.8 A3.3 3.3 0 0 1 5 0.5 Z"/></svg>
      <span>Halvorn Kitchens<br>48 Marlow Street<br>Eastbridge<br>EB4 2KL</span>
    </address>
  </section>

</body>
</html>
```